HLD business cards Dr. Martin Voss

I need a business card designed for our dental office. We are a "general dental" practice.
Looking for a clean, professional but not too fancy design with our logo and contact information required.
front of card is information/standard business card, backside is appt reminder with lines for date and time of appt
doctors name: Dr. Martin Voss DMD
office name: Voss Family Dental
address: 4827 N Birchwell Ave Linden Harbor, FL 32190
phone: 321-555-0173
Contact Information for Business Card
Office name, Doctor name, address, phone number...etc
- White/off white base color, blue and or black lettering

```html
<!DOCTYPE html>
<html lang="en">
<head>
<meta charset="utf-8">
<title>Voss Family Dental – Business Card</title>
<link href="https://fonts.googleapis.com/css2?family=Crimson+Text:wght@400;700&display=swap" rel="stylesheet">
<style>
  :root {
    --backdrop: #adacad;
    --card: #ffffff;
    --ink: #1e1e1e;
    --rule-grey: #8a8a8a;
    --band: #0f0f0f;
  }
  * { box-sizing: border-box; margin: 0; padding: 0; }
  html, body { width: 995px; height: 1200px; overflow: hidden; }
  body {
    background: var(--backdrop);
    font-family: "Crimson Text", Georgia, serif;
    color: var(--ink);
    position: relative;
  }
  .card {
    position: absolute;
    left: 125px;
    width: 745px;
    height: 425px;
    background: var(--card);
    border-radius: 22px;
    overflow: hidden;
  }
  .card--appointment { top: 142px; }
  .card--contact { top: 635px; }
  .card-band {
    position: absolute; left: 0; right: 0; bottom: 0; height: 16px;
    background: var(--band);
    border-top: 3px solid var(--rule-grey);
    box-shadow: 0 -4px 0 var(--card);
  }

  /* Appointment side */
  .appointment-title {
    position: absolute; top: 34px; left: 0; right: 0;
    text-align: center; font-weight: 700; font-size: 31px; letter-spacing: 0.3px;
  }
  .field-row {
    position: absolute; left: 43px; right: 44px;
    display: flex; align-items: baseline; font-size: 21px; white-space: nowrap;
  }
  .blank {
    height: 2px; align-self: flex-end; margin: 0 10px 7px;
    background: repeating-linear-gradient(90deg, var(--ink) 0 10px, transparent 10px 18px);
  }
  .blank--name { flex: 1; margin-left: 6px; }
  .blank--day, .blank--date { flex: 135; }
  .blank--time { flex: 100; margin-left: 4px; }
  .row-patient { top: 118px; }
  .row-1 { top: 176px; }
  .row-2 { top: 225px; }
  .row-3 { top: 274px; }
  .weekday-list {
    position: absolute; top: 339px; left: 0; right: 0;
    display: flex; justify-content: center; gap: 38px; font-size: 22px;
  }
  .weekday { display: flex; align-items: center; gap: 16px; }
  .checkbox { width: 20px; height: 20px; border: 1.5px solid var(--ink); }

  /* Contact side */
  .practice-mark {
    position: absolute; top: 120px; left: 0; right: 0;
    display: flex; justify-content: center; align-items: center; gap: 12px;
    font-size: 34px; font-weight: 400; color: var(--ink);
  }
  .practice-dot { width: 14px; height: 14px; border-radius: 50%; background: var(--ink); }
  .doctor-name {
    position: absolute; top: 272px; left: 0; right: 0;
    text-align: center; font-weight: 700; font-size: 27px;
  }
  .contact-line {
    position: absolute; left: 0; right: 0;
    display: flex; justify-content: center; align-items: center; gap: 4px;
    font-size: 17px;
  }
  .contact-phone { top: 326px; }
  .contact-address { top: 350px; }
  .contact-line svg { width: 11px; height: 12px; fill: var(--ink); }
</style>
</head>
<body>
  <section class="card card--appointment">
    <h2 class="appointment-title">YOUR NEXT APPOINTMENT</h2>
    <div class="field-row row-patient">Patient name:<span class="blank blank--name"></span></div>
    <div class="field-row row-1">Day:<span class="blank blank--day"></span>Date:<span class="blank blank--date"></span>Time<span class="blank blank--time"></span>AM/PM</div>
    <div class="field-row row-2">Day:<span class="blank blank--day"></span>Date:<span class="blank blank--date"></span>Time<span class="blank blank--time"></span>AM/PM</div>
    <div class="field-row row-3">Day:<span class="blank blank--day"></span>Date:<span class="blank blank--date"></span>Time<span class="blank blank--time"></span>AM/PM</div>
    <div class="weekday-list">
      <span class="weekday"><span class="checkbox"></span>Mon</span>
      <span class="weekday"><span class="checkbox"></span>Tue</span>
      <span class="weekday"><span class="checkbox"></span>Wed</span>
      <span class="weekday"><span class="checkbox"></span>Thu</span>
      <span class="weekday"><span class="checkbox"></span>Fri</span>
    </div>
    <div class="card-band"></div>
  </section>

  <section class="card card--contact">
    <div class="practice-mark"><span class="practice-dot"></span>Voss Family Dental</div>
    <h1 class="doctor-name">DR. MARTIN VOSS DMD</h1>
    <p class="contact-line contact-phone">
      <svg viewBox="0 0 24 24" aria-hidden="true"><path d="M6.6 10.8c1.4 2.8 3.8 5.1 6.6 6.6l2.2-2.2c.3-.3.7-.4 1-.2 1.1.4 2.3.6 3.6.6.6 0 1 .4 1 1V20c0 .6-.4 1-1 1C10.6 21 3 13.4 3 4c0-.6.4-1 1-1h3.5c.6 0 1 .4 1 1 0 1.3.2 2.5.6 3.6.1.3 0 .7-.2 1L6.6 10.8z"/></svg>
      321-555-0173
    </p>
    <p class="contact-line contact-address">
      <svg viewBox="0 0 24 24" aria-hidden="true"><path d="M12 2C8.1 2 5 5.1 5 9c0 5.2 7 13 7 13s7-7.8 7-13c0-3.9-3.1-7-7-7zm0 9.5a2.5 2.5 0 1 1 0-5 2.5 2.5 0 0 1 0 5z"/></svg>
      4827 N Birchwell Ave Linden Harbor, FL 32190
    </p>
    <div class="card-band"></div>
  </section>
</body>
</html>
```